Business Card Design Project

We need a business card for a new technology services company. We develop software and implement software packages for our business customers and although we will begin with just one or two service offerings, our service offerings will expand over time. Our name comes from the an author, RK Bellowes, and his "idea" was that opportunity should be based on ability and achievement, not on social status.

We would like to see a design that is standard in its size and shape, but stands apart in its dramatic color contrasts. The card should not use too many colors - the colors used in the background should highlight the brilliant blues of the logo (see attachment) to dramatic effect. The background should not be white.

If necessary, you can change the color of the words "RK Bellowes", but not the word "Idea".

Card size should be U.S. standard 2 inches by 3.5 inches and provide for 1/8 inch bleed area on each side.

We need a design for both sides of the business card, one side communicating the company logo and contact information, the other side being purely graphical, incorporating the logo but no other information.

Contact Information Required:
Mark Linden
MarkLinden@rkbellowesidea.com
555-304-7812

Target Market(s)

Business executives

Industry/Entity Type

Software

Requirements
Must have
• It must have the full company logo on one side, and at least the graphic element of the logo on the other. Either that or the full logo on both.
Nice to have
• It would be nice to have a design that could work without needing two different textures. For example, it would be nice if the entire card could be shiny, not just parts of the card.

It would also be nice if texture is something we could add later.
Should not have
• The card should not use the color green.

```html
<!DOCTYPE html>
<html lang="en">
<head>
<meta charset="utf-8">
<title>RK Bellowes – Business Card</title>
<link rel="stylesheet" href="https://fonts.googleapis.com/css2?family=Inter:wght@300&display=swap">
<style>
  :root {
    --stage: #1a1a1b;
    --card-gray: #454547;
    --band: #231f20;
    --blue-deep: #0070b0;
    --blue-mid: #0a86c6;
    --blue-light: #8fbde3;
    --accent-blue: #1ea0e0;
    --text-light: #f2f2f2;
  }
  * { margin: 0; padding: 0; box-sizing: border-box; }
  html, body {
    width: 1200px;
    height: 800px;
    overflow: hidden;
    background: var(--stage);
    font-family: "Inter", "Helvetica Neue", Arial, sans-serif;
  }
  .sheet {
    width: 1200px;
    height: 800px;
    display: flex;
    align-items: center;
    justify-content: center;
    gap: 50px;
  }
  .card {
    width: 525px;
    height: 300px;
    border-radius: 3px;
    overflow: hidden;
    position: relative;
    box-shadow: 0 10px 30px rgba(0,0,0,.55);
  }
  .card-front svg { display: block; }
  .brand-name {
    font-family: "Inter", "Helvetica Neue", Arial, sans-serif;
    font-weight: 300;
    font-size: 32px;
    letter-spacing: -0.6px;
    fill: var(--text-light);
  }
  .brand-dot { fill: var(--accent-blue); }

  .card-back { background: var(--card-gray); }
  .back-mark {
    position: absolute;
    left: 44px;
    top: 40px;
    display: flex;
    align-items: center;
    gap: 10px;
    color: var(--text-light);
    font-weight: 300;
    font-size: 15px;
  }
  .back-mark .mark-dot {
    width: 22px; height: 22px;
    border-radius: 50%;
    background: var(--accent-blue);
  }
  .contact {
    position: absolute;
    right: 40px;
    bottom: 52px;
    color: var(--text-light);
    font-weight: 300;
    font-size: 18px;
    line-height: 1.55;
  }
  .contact-name {
    text-align: right;
    font-size: 22px;
    letter-spacing: .5px;
    margin-bottom: 10px;
  }
  .contact-row { display: flex; align-items: center; gap: 8px; }
  .contact-rule {
    width: 62px;
    height: 1px;
    background: var(--text-light);
    margin-right: 16px;
  }
  .contact-rule.spacer { background: transparent; }
  .contact-label { color: var(--accent-blue); }
</style>
</head>
<body>
<main class="sheet">

  <section class="card card-front" aria-label="Card front">
    <svg width="525" height="300" viewBox="0 0 525 300" xmlns="http://www.w3.org/2000/svg">
      <defs>
        <linearGradient id="frontBlue" x1="0" y1="0" x2="0.35" y2="1">
          <stop offset="0" stop-color="var(--blue-deep)"/>
          <stop offset="0.55" stop-color="var(--blue-mid)"/>
          <stop offset="1" stop-color="var(--blue-light)"/>
        </linearGradient>
      </defs>
      <rect class="front-field" width="525" height="300" fill="url(#frontBlue)"/>
      <polygon class="front-band" points="0,12 0,118 525,292 525,186" fill="var(--band)"/>
      <g transform="translate(26 72) rotate(18.3)">
        <text class="brand-name" x="0" y="0">RK Bellowes</text>
        <circle class="brand-dot" cx="212" cy="-11" r="14"/>
      </g>
    </svg>
  </section>

  <section class="card card-back" aria-label="Card back">
    <div class="back-mark">
      <span class="mark-dot"></span>
      <span>RK Bellowes</span>
    </div>
    <div class="contact">
      <p class="contact-name">Mark Linden</p>
      <p class="contact-row"><span class="contact-rule"></span><span class="contact-label">E.</span> MarkLinden@rkbellowesidea.com</p>
      <p class="contact-row"><span class="contact-rule spacer"></span><span class="contact-label">P.</span> 555-304-7812</p>
    </div>
  </section>

</main>
</body>
</html>
```